Modern & Simple Essential Oils Label

Company Name: Meadowlark Essentials

What we sell: Aromatherapy products, pure therapeutic essential oils.

Design need:
We are looking for a creative and youthful design for the labels used on small essentials oils.

I have two sizes of bottles that I use for essential oils a 5ml bottle and a 15ml bottle. They are dark Amber color glass with black lids. I like the clear labels or mayble a dark brown background. With white or clear lettering with punch of color too! Each oil type is represented by different color. (lavender- purple, lemon - yellow). The label will be the same for all the oils in the two sizes with only a different oil name & coordinating color.
5ml label size should be: 1 " x 2.625"
15ml label size should be: 1.5" x 3.5"

I have some labels that I have had another designer start on, but they aren't quite what I want and missing that something (alot!).. I don't know what. Interest maybe? Lack of design? I dunno.. they are attached. Maybe it's the logo? I don't know! But its gotta change! When I cut out a proof and put a sample on the bottle as I look straight on at the label all I see is a big dot, no logo.. nothing interesting.
Updates

Project Deadline Extended
Reason: Hi! Id like to extend this deadline. Ive been unavailable for a few days due to an illness and Im so far behind! Im feeling MUCH better and looking forward to getting caught up and move with the project. Im not sure how this works, but I attached a list of the oils that we currently have available. And in the list is the idea for the color schemes for the oils. The basic idea is for it to have a wide array of colors, so using different shades of greens, yellows, oranges and so on. So that its like a rainbow. We are not set of that particular color for that particular oil. It was just a idea list of possible colors for oils. Thanks so much!

Target Market(s)

Metro & Modern people. Interested in healthy organic living, Mostly women (some men) 20-45 who are interested in holistic healing.

Industry/Entity Type

It Company

Requirements
Must have
• A reputable look. Clean, organic, crisp, zen or spa-like feel. Modern, youthful appealing label design. Approachable and interesting, not intimidating so that I don't turn away people who are new or not familiar with how to use essential oils.
Should not have
• do NOT want the look to be anywhere close to medicinal, witchy, crafty, hippie, mystical, overly earthy, magical, or voodoo. Do not want it to look like something out of a grandmothers medicine cabinet.

```html
<!DOCTYPE html>
<html lang="en">
<head>
<meta charset="utf-8">
<title>Meadowlark Essentials – Essential Oil Labels</title>
<link href="https://fonts.googleapis.com/css2?family=Josefin+Sans:wght@300;400&family=Lora:ital@1&family=Open+Sans:wght@400&display=swap" rel="stylesheet">
<style>
  :root {
    --canvas: #ffffff;
    --band-dark: #1c1a19;
    --ink: #3a3a3a;
    --ink-light: #e9e4ef;
    --white: #ffffff;
    --bergamot: #7cbd3b;
    --lemon: #f3e11c;
    --cinnamon: #ec4a12;
    --patchouli: #8e2f9c;
    --ylang: #5b2a8e;
    --peppermint: #1f3f86;
  }
  * { margin: 0; padding: 0; box-sizing: border-box; }
  html, body { width: 1200px; height: 851px; overflow: hidden; background: var(--canvas); }
  .canvas { position: relative; width: 1200px; height: 851px; }

  .label {
    position: absolute;
    display: flex;
    flex-direction: column;
    align-items: center;
    background: var(--oil);
    overflow: hidden;
  }
  .label__brand {
    flex: 1;
    display: flex;
    flex-direction: column;
    align-items: center;
    justify-content: center;
    font-family: "Josefin Sans", sans-serif;
    font-weight: 400;
    color: var(--white);
    text-align: center;
    letter-spacing: 0.08em;
    text-transform: uppercase;
    line-height: 1.25;
  }
  .label__name-band {
    width: 100%;
    background: rgba(255,255,255,0.22);
    text-align: center;
  }
  .label__oil {
    font-family: "Josefin Sans", sans-serif;
    font-weight: 300;
    color: var(--ink);
    letter-spacing: 0.06em;
    text-transform: uppercase;
    white-space: nowrap;
    line-height: 1.2;
  }
  .label__latin {
    font-family: "Lora", serif;
    font-style: italic;
    color: var(--ink);
    white-space: nowrap;
  }
  .label__volume {
    width: 100%;
    background: var(--band-dark);
    color: var(--white);
    font-family: "Open Sans", sans-serif;
    text-align: center;
    white-space: nowrap;
  }

  /* 15 ml label */
  .label--large { left: 155px; top: 305px; width: 242px; height: 393px; }
  .label--large .label__brand { font-size: 21px; }
  .label--large .label__name-band { padding: 8px 0 10px; margin-bottom: 20px; }
  .label--large .label__oil { font-size: 30px; }
  .label--large .label__latin { font-size: 16px; margin-top: 2px; }
  .label--large .label__volume { font-size: 14px; padding: 14px 0; }

  /* 5 ml labels */
  .label--small { top: 395px; width: 103px; height: 145px; }
  .label--small .label__brand { font-size: 9px; }
  .label--small .label__name-band { padding: 4px 6px 5px; margin-bottom: 10px; }
  .label--small .label__oil { font-size: 10px; letter-spacing: 0.02em; }
  .label--small .label__latin { font-size: 6px; margin-top: 1px; }
  .label--small .label__volume { font-size: 6px; padding: 5px 0; }

  .label--lemon { left: 519px; --oil: var(--lemon); }
  .label--cinnamon { left: 641px; --oil: var(--cinnamon); }
  .label--patchouli { left: 765px; --oil: var(--patchouli); }
  .label--ylang { left: 889px; --oil: var(--ylang); }
  .label--peppermint { left: 1013px; --oil: var(--peppermint); }
  .label--bergamot { --oil: var(--bergamot); }
  .label--ylang .label__oil, .label--ylang .label__latin,
  .label--peppermint .label__oil, .label--peppermint .label__latin,
  .label--patchouli .label__oil, .label--patchouli .label__latin { color: var(--ink-light); }
</style>
</head>
<body>
<main class="canvas">
  <section class="label label--large label--bergamot">
    <div class="label__brand">Meadowlark<br>Essentials</div>
    <div class="label__name-band">
      <p class="label__oil">Bergamot</p>
      <p class="label__latin">citrus bergamia</p>
    </div>
    <p class="label__volume">15 ml (0.5 US FL OZ)</p>
  </section>

  <section class="label label--small label--lemon">
    <div class="label__brand">Meadowlark<br>Essentials</div>
    <div class="label__name-band">
      <p class="label__oil">Lemon</p>
      <p class="label__latin">citrus limonum</p>
    </div>
    <p class="label__volume">15 ml (0.5 US FL OZ)</p>
  </section>

  <section class="label label--small label--cinnamon">
    <div class="label__brand">Meadowlark<br>Essentials</div>
    <div class="label__name-band">
      <p class="label__oil">Cinnamon Bark</p>
      <p class="label__latin">Cinnamomum zeylanicum</p>
    </div>
    <p class="label__volume">15 ml (0.5 US FL OZ)</p>
  </section>

  <section class="label label--small label--patchouli">
    <div class="label__brand">Meadowlark<br>Essentials</div>
    <div class="label__name-band">
      <p class="label__oil">Patchouli</p>
      <p class="label__latin">pogostemon cablin</p>
    </div>
    <p class="label__volume">15 ml (0.5 US FL OZ)</p>
  </section>

  <section class="label label--small label--ylang">
    <div class="label__brand">Meadowlark<br>Essentials</div>
    <div class="label__name-band">
      <p class="label__oil">Ylang Ylang</p>
      <p class="label__latin">cananga odorata</p>
    </div>
    <p class="label__volume">15 ml (0.5 US FL OZ)</p>
  </section>

  <section class="label label--small label--peppermint">
    <div class="label__brand">Meadowlark<br>Essentials</div>
    <div class="label__name-band">
      <p class="label__oil">Peppermint</p>
      <p class="label__latin">mentha piperita</p>
    </div>
    <p class="label__volume">15 ml (0.5 US FL OZ)</p>
  </section>
</main>
</body>
</html>
```